Brand-new Pediatric Dental Practice needs a website

We are a brand-new dental practice that will specialize in treating children. We want a gorgeous and easily navigable dental practice website that would make a good first impression to potential patients and their parents. It should be modern, SEO-friendly, mobile responsive, and optimized to win new patients.

Target Market(s)

Parents

Industry/Entity Type

Healthcare/Dentistry

Coding

Coded - Design and coding required

Number of Pages Required

4 page

Requirements
Must have
• Use the Wix website building platform. 4 pages: home, meet our dentists, services, contact us
Nice to have
• has a link to our facebook, instagram

```html
<!DOCTYPE html>
<html lang="en">
<head>
<meta charset="utf-8">
<title>Maple Grove Pediatric Dentistry</title>
<link href="https://fonts.googleapis.com/css2?family=Kumbh+Sans:wght@400;500;600;700&display=swap" rel="stylesheet">
<style>
:root{
  --ink:#151515;
  --text:#555;
  --muted:#777;
  --red:#f03a4f;
  --red2:#ff6272;
  --green:#3aa564;
  --soft:#f1f3f8;
  --field:#f3f5f9;
  --footer:#343434;
  --white:#fff;
}
*{box-sizing:border-box;margin:0;padding:0}
html,body{width:1200px;height:3829px;overflow:hidden}
body{font-family:"Kumbh Sans",sans-serif;color:var(--ink);background:var(--white);position:relative}
.btn{position:absolute;display:flex;align-items:center;justify-content:center;gap:6px;border-radius:4px;color:var(--white);font-size:13px;font-weight:500;letter-spacing:.2px;background:linear-gradient(90deg,var(--red),var(--red2));box-shadow:0 6px 14px rgba(240,58,79,.25)}
.ring{width:15px;height:15px;border:1px solid currentColor;border-radius:50%;display:inline-flex;align-items:center;justify-content:center;font-size:10px}
.eyebrow{position:absolute;font-size:12px;font-weight:600;text-transform:uppercase;letter-spacing:.2px;display:flex;align-items:center;gap:10px}
.eyebrow::before{content:"";width:30px;height:1px;background:var(--ink)}
.eyebrow.center::after{content:"";width:30px;height:1px;background:var(--ink)}
h1,h2{font-weight:600;line-height:1.22}
.photo{position:absolute}

/* header */
.header{position:absolute;top:0;left:0;width:1200px;height:110px}
.brand{position:absolute;left:86px;top:20px;width:140px}
.brand .mark{width:40px;height:40px;border-radius:50%;background:var(--green);margin-left:38px}
.brand .name{font-size:24px;font-weight:500;color:#3d3d3d;line-height:1;margin-top:6px}
.brand .sub{font-size:7px;letter-spacing:2px;color:#3d3d3d;margin-top:2px}
.nav{position:absolute;top:46px;font-size:15px;font-weight:500}
.sq{position:absolute;width:42px;height:42px;background:#2d2d2d;border-radius:3px;display:flex;align-items:center;justify-content:center}
.sq i{width:10px;height:10px;border:1.5px solid var(--white);border-radius:50%}

/* hero */
.hero{position:absolute;top:110px;left:0;width:1200px;height:540px;background:linear-gradient(90deg,#f2f2f2,#e9e9e9)}
.hero-photo{left:560px;top:0;width:640px;height:540px;background:radial-gradient(ellipse at 55% 40%,#efe7de,#e4e2df 70%)}
.hero h1{position:absolute;left:84px;top:155px;font-size:46px;width:520px}
.hero p{position:absolute;left:86px;top:288px;width:445px;font-size:13px;line-height:21px;color:var(--text)}

/* about */
.about-big{left:86px;top:730px;width:414px;height:410px;background:linear-gradient(160deg,#e3b540,#c99a2c 45%,#2d3b52 70%)}
.about-small{left:80px;top:968px;width:199px;height:221px;border:6px solid var(--white);background:linear-gradient(160deg,#c7b7a4,#6f6257 60%,#ddd)}
.about h2{position:absolute;left:558px;top:790px;font-size:42px;width:440px}
.about .lead{position:absolute;left:559px;top:906px;width:530px;font-size:13px;line-height:21px;color:#333}
.feat{position:absolute;top:992px;display:flex;align-items:center;gap:10px;font-size:20px;font-weight:500}
.about .note{position:absolute;left:559px;top:1045px;width:520px;font-size:13px;line-height:21px;color:var(--text)}

/* services */
.services{position:absolute;top:1274px;left:0;width:1200px;height:611px;background:var(--soft)}
.services h2{position:absolute;top:108px;width:1200px;text-align:center;font-size:42px}
.card{position:absolute;top:187px;width:238px;height:323px;background:var(--white);text-align:center}
.card .img{margin:14px auto 0;width:210px;height:157px}
.card h3{font-size:21px;font-weight:500;margin-top:22px}
.card p{font-size:13px;line-height:17px;color:var(--muted);width:178px;margin:12px auto 0}
.go{position:absolute;left:97px;bottom:-22px;width:44px;height:44px;border-radius:50%;background:var(--green);display:flex;align-items:center;justify-content:center}

/* team */
.team h2{position:absolute;left:84px;top:1982px;font-size:42px;width:560px}
.doc{position:absolute;top:2112px;width:326px;height:454px;background:var(--white);box-shadow:0 10px 30px rgba(0,0,0,.08);text-align:center}
.doc .img{width:326px;height:294px}
.doc h3{font-size:21px;font-weight:500;margin-top:30px}
.doc .role{font-size:13px;color:var(--muted);margin-top:6px}
.dots{display:flex;justify-content:center;gap:12px;margin-top:18px}
.dots span{width:42px;height:42px;border-radius:50%;background:var(--green);display:flex;align-items:center;justify-content:center}
.dots i{width:10px;height:10px;border:1.5px solid var(--white);border-radius:50%}

/* cta band */
.band{position:absolute;top:2647px;left:0;width:1200px;height:235px;background:var(--green)}
.band h2{position:absolute;left:85px;top:64px;font-size:42px;color:var(--white);width:640px}
.band .ghost{position:absolute;left:977px;top:95px;width:137px;height:45px;background:var(--white);border-radius:4px;color:var(--green);font-size:13px;font-weight:500;display:flex;align-items:center;justify-content:center;gap:6px}

/* appointment */
.appoint h2{position:absolute;top:3003px;width:1200px;text-align:center;font-size:42px}
.field{position:absolute;top:3068px;height:52px;width:204px;background:var(--field);font-size:15px;color:#888;padding:17px 19px}
.area{position:absolute;left:174px;top:3138px;width:852px;height:142px;background:var(--field);font-size:15px;color:#888;padding:17px 19px}

/* footer */
.footer{position:absolute;top:3428px;left:0;width:1200px;height:401px;background:var(--footer);color:var(--white)}
.footer .brand{left:86px;top:70px}
.footer .brand .name,.footer .brand .sub{color:var(--white)}
.footer .about-text{position:absolute;left:86px;top:162px;width:250px;font-size:13px;line-height:21px}
.fsq{position:absolute;top:238px;width:42px;height:42px;background:#4a4a4a;display:flex;align-items:center;justify-content:center}
.fsq i{width:10px;height:10px;border:1.5px solid var(--white);border-radius:50%}
.col{position:absolute;top:70px}
.col h4{font-size:22px;font-weight:400;margin-bottom:24px}
.col li{list-style:none;font-size:13px;line-height:14px;margin-bottom:19px}
.footer .rule{position:absolute;left:0;top:336px;width:1200px;height:1px;background:#4a4a4a}
.footer .copy{position:absolute;top:362px;width:1200px;text-align:center;font-size:13px}
</style>
</head>
<body>

<header class="header">
  <div class="brand"><div class="mark"></div><div class="name">maple grove</div><div class="sub">PEDIATRIC DENTISTRY</div></div>
  <nav>
    <span class="nav" style="left:543px">Home</span>
    <span class="nav" style="left:627px">Meet Our Dentists</span>
    <span class="nav" style="left:801px">Services</span>
    <span class="nav" style="left:901px">Contact Us</span>
  </nav>
  <a class="sq" style="left:1017px;top:34px" aria-label="Social profile"><i></i></a>
  <a class="sq" style="left:1072px;top:34px" aria-label="Photo profile"><i></i></a>
</header>

<section class="hero">
  <div class="photo hero-photo" role="img" aria-label="Smiling boy brushing a large cut-out tooth"></div>
  <div class="eyebrow" style="left:86px;top:122px">Partnership for health</div>
  <h1>Modern Dentistry with Unique Technologies</h1>
  <p>Lorem Ipsum is simply dummy text of the printing and typesetting industry. Lorem Ipsum has been the industry's standard dummy text ever since Athe 1500s</p>
  <a class="btn" style="left:86px;top:376px;width:137px;height:45px">READ MORE <span class="ring">›</span></a>
</section>

<section class="about">
  <div class="photo about-big" role="img" aria-label="Child sitting in a yellow dental chair"></div>
  <div class="photo about-small" role="img" aria-label="Dentist examining a child's teeth"></div>
  <div class="eyebrow" style="left:560px;top:766px">What about us</div>
  <h2>We Provide the Best Dental Service</h2>
  <p class="lead">Lorem Ipsum is simply dummy text of the printing and typesetting industry. Lorem Ipsum has been the industry's standard dummy text ever since the 1500s, when an unknown printer</p>
  <div class="feat" style="left:559px">
    <svg width="42" height="36" viewBox="0 0 42 36" fill="none" stroke="#3aa564" stroke-width="1.6"><path d="M4 8c3-6 10-4 13-2 3-2 10-4 13 2 2 5-2 12-3 18-1 5-4 6-5 0-1-4-3-4-4 0-1 6-5 5-6 0-1-6-6-12-8-18z"/><circle cx="32" cy="26" r="6"/><path d="M32 23v6M29 26h6"/></svg>
    Dental Prevention
  </div>
  <div class="feat" style="left:820px">
    <svg width="40" height="36" viewBox="0 0 40 36" fill="none" stroke="#3aa564" stroke-width="1.6"><path d="M5 6c3-5 10-3 14-1 4-2 11-4 14 1 2 5-2 12-3 18-1 6-4 7-6 0-1-4-3-4-4 0-2 7-5 6-6 0-1-6-8-13-9-18z"/></svg>
    Dental Services
  </div>
  <p class="note">Lorem Ipsum is simply dummy text of the printing and typesetting industry. Lorem Ipsum has been the industry's standard dummy text</p>
  <a class="btn" style="left:559px;top:1113px;width:138px;height:45px">READ MORE <span class="ring">›</span></a>
</section>

<section class="services">
  <div class="eyebrow center" style="left:508px;top:80px">Our services</div>
  <h2>Explore Our Main Service</h2>
  <div class="card" style="left:85px">
    <div class="img" role="img" aria-label="Girl in an orange dental chair during a filling" style="background:linear-gradient(120deg,#c9b98a,#f08a1e 55%,#e8e2d8)"></div>
    <h3>Dental Filling</h3><p>There are many variations of pas of Lorem Ipsum available.</p>
    <span class="go"><svg width="18" height="12" viewBox="0 0 18 12" fill="none" stroke="#fff" stroke-width="1.5"><path d="M1 6h15M11 1l5 5-5 5"/></svg></span>
  </div>
  <div class="card" style="left:350px">
    <div class="img" role="img" aria-label="Hands holding a tooth model showing root canals" style="background:linear-gradient(135deg,#9fb8e6,#e9c9d8 55%,#6f90c9)"></div>
    <h3>Root Canal</h3><p>There are many variations of pas of Lorem Ipsum available.</p>
    <span class="go"><svg width="18" height="12" viewBox="0 0 18 12" fill="none" stroke="#fff" stroke-width="1.5"><path d="M1 6h15M11 1l5 5-5 5"/></svg></span>
  </div>
  <div class="card" style="left:612px">
    <div class="img" role="img" aria-label="Young girl seated in a blue dental chair" style="background:linear-gradient(135deg,#cfd8e0,#8fa7bc 50%,#e9e4df)"></div>
    <h3>Dental Implant</h3><p>There are many variations of pas of Lorem Ipsum available.</p>
    <span class="go"><svg width="18" height="12" viewBox="0 0 18 12" fill="none" stroke="#fff" stroke-width="1.5"><path d="M1 6h15M11 1l5 5-5 5"/></svg></span>
  </div>
  <div class="card" style="left:878px">
    <div class="img" role="img" aria-label="Gloved hands holding a dental model with braces" style="background:linear-gradient(135deg,#dfe6ee,#e07a86 50%,#cfd9e4)"></div>
    <h3>Braces &amp; Aligners</h3><p>There are many variations of pas of Lorem Ipsum available.</p>
    <span class="go"><svg width="18" height="12" viewBox="0 0 18 12" fill="none" stroke="#fff" stroke-width="1.5"><path d="M1 6h15M11 1l5 5-5 5"/></svg></span>
  </div>
</section>

<section class="team">
  <div class="eyebrow" style="left:86px;top:1964px">Our dentist</div>
  <h2>Meet Our Specialized and Experienced Dentist</h2>
  <a class="btn" style="left:977px;top:2037px;width:137px;height:46px">VIEW ALL</a>
  <div class="doc" style="left:86px">
    <div class="img" role="img" aria-label="Portrait of a male dentist in a white coat" style="background:linear-gradient(180deg,#f4f4f4,#e6e9ee)"></div>
    <h3>Dr. Aaron Whitfield</h3><div class="role">Prosthodontics Dentist</div>
    <div class="dots"><span aria-label="Social profile"><i></i></span><span aria-label="Photo profile"><i></i></span></div>
  </div>
  <div class="doc" style="left:436px">
    <div class="img" role="img" aria-label="Portrait of a female dentist in blue scrubs" style="background:linear-gradient(180deg,#3fc3e6,#2aa9d8)"></div>
    <h3>Dr. Aaron Whitfield</h3><div class="role">Prosthodontics Dentist</div>
    <div class="dots"><span aria-label="Social profile"><i></i></span><span aria-label="Photo profile"><i></i></span></div>
  </div>
  <div class="doc" style="left:789px">
    <div class="img" role="img" aria-label="Portrait of a male dentist holding a dental model" style="background:linear-gradient(180deg,#d9dadb,#e8e8e8)"></div>
    <h3>Dr. Aaron Whitfield</h3><div class="role">Prosthodontics Dentist</div>
    <div class="dots"><span aria-label="Social profile"><i></i></span><span aria-label="Photo profile"><i></i></span></div>
  </div>
</section>

<section class="band">
  <h2>A great place of medical hospital center &amp; dental care</h2>
  <a class="ghost">CONTACT US <span class="ring">›</span></a>
</section>

<section class="appoint">
  <div class="eyebrow center" style="left:509px;top:2960px">Appointment</div>
  <h2>Apply for free Dental Checkup</h2>
  <div class="field" style="left:174px">Your Name</div>
  <div class="field" style="left:390px">Gender</div>
  <div class="field" style="left:606px">Your Email</div>
  <div class="field" style="left:822px">Phone No.</div>
  <div class="area">Your Message</div>
  <a class="btn" style="left:534px;top:3302px;width:132px;height:44px">SEND MESSAGE</a>
</section>

<footer class="footer">
  <div class="brand"><div class="mark" style="margin-left:32px"></div><div class="name" style="font-size:21px">maple grove</div><div class="sub">PEDIATRIC DENTISTRY</div></div>
  <p class="about-text">It helps designers plan out where the content will sit, the content to be written and approved.</p>
  <a class="fsq" style="left:86px" aria-label="Social profile"><i></i></a>
  <a class="fsq" style="left:140px" aria-label="Photo profile"><i></i></a>
  <div class="col" style="left:437px"><h4>Main Menu</h4><ul><li>Home</li><li>About Us</li><li>Meet Our Dentists</li><li>Services</li><li>Contact</li></ul></div>
  <div class="col" style="left:646px"><h4>Quick Links</h4><ul><li>FAQ</li><li>Doctors</li><li>Departments</li><li>Events</li><li>Member</li></ul></div>
  <div class="col" style="left:855px;width:270px"><h4>Contact</h4><ul><li>Call : +1800-555-0147</li><li>Email : hello@maplegrove-kids.com</li><li style="line-height:19px">Location : Lorem ipsum dolor sit amet, consectetur adipiscing elit.</li></ul></div>
  <div class="rule"></div>
  <div class="copy">Copyright 2022 Maple Grove. All Rights Reserved</div>
</footer>

</body>
</html>
```